Business Identity Stationary

Already have the logo which is in the attached files so only need the Business STationary
1) Double Sided Business Card
2) Letterhead
3) Presentation folder with business card holder on inside cover
4) WIth compliments slip
See information for business cards, letterhead and presentation folder below.
http://files.pixelbazaar-example.com/img/771204/40612/40612_3918825_771204_thumb.jpg
Updates

This should be a simply job using a logo we already had designed along with a little device. I suggest using the device off center and perhaps lower in the corner in an abstract way. Also the logo device could be used as a watermark for the letterhead. The designer who created the logo presented something that I think works well for a business card. The front of the double sided business card could have the name logo small for the website address and only use the Lime device on the front. Then on the back could be the name Brevar Consulting logo.

Please note that for the business card the black and lime green background do look good. Also please think of using the lime device separately in an unusual way.

It has been brought to my attention that.my budget was far to low. Hopefully this.will attract you to the project. 

The parent company of Brevar Consulting is TallHeron investments. I have uploaded a file of the Tall Heron business card I really like. Perhaps use this business card as a guide to the type of modern and clean style I am looking for. It also works to have the Brevar Consultign and Tall Heron similar.

Reason: Still haven't received anything exactly right.

Industry/Entity Type

Business

Font styles to use
Sans Serif

Colors
9bcb3c
000000
5c5c5c
add136
cadf82
eaf2cf
f9fbf2
1b1b1b
757575

Requirements
Must have
• 1) Double Sided Business Card
Marta Delvorin
Director
Tel: +505 8290 3357
Email: mkd@brevarconsulting-example.com
Website: www.brevarconsulting-example.com

Everett Delvorin
Director
Tel: +505 8290 3362
Email: ekd@brevarconsulting-example.com

Lucia Pardo Ventrosa
Director
Tel: 8442 6183
Email: lpv@brevarconsulting-example.com

2) Letterhead
Logo
Lime Logo Device
Website Address: www.brevarconsulting-example.com
Small print on bottom: Brevar Consulting a Tall Heron Investment Company SA. RUC K0720000483915

3) Presentation Folder
Traditional Presentation folder with inside front cover spot for the insertion of business card.

4) With Compliments slip

```html
<!DOCTYPE html>
<html lang="en">
<head>
<meta charset="utf-8">
<title>Brevar Consulting Letterhead</title>
<link href="https://fonts.googleapis.com/css2?family=Open+Sans:wght@400;600&display=swap" rel="stylesheet">
<style>
  :root {
    --lime: #9bcb3c;
    --black: #000000;
    --ink: #1b1b1b;
    --grey: #5c5c5c;
    --backdrop: #e6e6e3;
    --paper: #ffffff;
    --band-top: #2a2a2a;
    --band-bottom: #0a0a0a;
  }
  html, body {
    margin: 0;
    padding: 0;
    width: 1200px;
    height: 1024px;
    overflow: hidden;
    background: var(--backdrop);
    font-family: "Open Sans", Arial, sans-serif;
  }
  .letterhead {
    position: absolute;
    left: 280px;
    top: 58px;
    width: 640px;
    height: 905px;
    background: var(--paper);
    box-shadow: 0 6px 24px rgba(0,0,0,0.18);
  }
  .brand {
    position: absolute;
    left: 52px;
    top: 50px;
    display: flex;
    align-items: center;
    gap: 10px;
  }
  .brand-name {
    font-size: 30px;
    font-weight: 400;
    color: var(--black);
    letter-spacing: 0.5px;
    line-height: 1;
  }
  .brand-dot {
    width: 16px;
    height: 16px;
    border-radius: 50%;
    background: var(--lime);
  }
  .contact {
    position: absolute;
    right: 46px;
    top: 128px;
    margin: 0;
    padding: 0;
    list-style: none;
    font-size: 10.5px;
    color: var(--ink);
    line-height: 15px;
  }
  .contact li {
    display: flex;
    align-items: center;
    gap: 5px;
  }
  .contact svg {
    width: 8px;
    height: 8px;
    flex: none;
  }
  .footer-band {
    position: absolute;
    left: 0;
    right: 0;
    bottom: 0;
    height: 52px;
    background: linear-gradient(180deg, var(--band-top), var(--band-bottom));
    display: flex;
    align-items: center;
    padding-left: 60px;
  }
  .footer-note {
    color: #ffffff;
    font-size: 11px;
    letter-spacing: 0.2px;
  }
</style>
</head>
<body>
  <main class="letterhead">
    <header class="brand">
      <span class="brand-name">Brevar Consulting</span>
      <span class="brand-dot"></span>
    </header>

    <ul class="contact">
      <li>
        <svg viewBox="0 0 10 10" aria-hidden="true"><path d="M2 1 L4 1 L4.6 3 L3.6 3.8 C4.2 5 5 5.8 6.2 6.4 L7 5.4 L9 6 L9 8 C5 8.5 1.5 5 2 1 Z" fill="var(--lime)"/></svg>
        <span>+505 8290 3357</span>
      </li>
      <li>
        <svg viewBox="0 0 10 10" aria-hidden="true"><rect x="0.5" y="2" width="9" height="6.5" fill="var(--lime)"/><path d="M0.5 2 L5 5.5 L9.5 2" fill="none" stroke="#fff" stroke-width="0.8"/></svg>
        <span>mkd@brevarconsulting-example.com</span>
      </li>
      <li>
        <svg viewBox="0 0 10 10" aria-hidden="true"><circle cx="5" cy="5" r="4.3" fill="var(--lime)"/><path d="M0.7 5 H9.3 M5 0.7 C2.8 3 2.8 7 5 9.3 M5 0.7 C7.2 3 7.2 7 5 9.3" fill="none" stroke="#fff" stroke-width="0.7"/></svg>
        <span>www.brevarconsulting-example.com</span>
      </li>
    </ul>

    <footer class="footer-band">
      <span class="footer-note">Brevar Consulting a Tall Heron Investment Company SA. RUC K0720000483915</span>
    </footer>
  </main>
</body>
</html>
```